Morvel & Morvel**

Liquid Magna-Min (400 mg) 4 oz
Liquid Ionic B12 (1,000 mcg) 2 oz
Probiotic 55 Billion 30 CT
Liquid Potassium 99mg
Liquid Iodide 225mcg
Liquid Strontium 100 mg
Liquid Iron 22mg
Liquid Ionic Zinc (50 mg) 2 oz
Liquid Ionic Selenium (300 mcg) 2 oz
Lonic Boron 6 mg
Fulvic Acid 250 mg
Chromium 550 mcg
Ox Bile 500 mg
Vitamin D3 1000 IU
Liver Support 1000 IU
Tonify blood 1000 IU
Adrenal Support 1000 IU
Constipation 1000 IU

Target Market(s)

public

Industry/Entity Type

Health And Wellness

Font styles to use
Serif

Requirements
Must have
• color
Nice to have
• I would like to see the designer's views.
Should not have
• I don't have any

```html
<!DOCTYPE html>
<html lang="en">
<head>
<meta charset="utf-8">
<title>Morvel &amp; Morvel Multi Vitamin Label</title>
<link href="https://fonts.googleapis.com/css2?family=Montserrat:wght@300;400;600;700;800&family=Oswald:wght@500;600&display=swap" rel="stylesheet">
<style>
  :root {
    --navy: #0b1462;
    --deep: #070b3a;
    --purple: #8f2b93;
    --violet: #6d2a8e;
    --ink: #111111;
    --tree-red: #d32a26;
    --tree-plum: #6a2486;
    --gold: #d9a21b;
    --green: #1f7a3a;
    --ribbon: #b3221d;
    --paper: #ffffff;
  }
  * { margin: 0; padding: 0; box-sizing: border-box; }
  html, body { width: 1200px; height: 1200px; overflow: hidden; background: var(--paper); }
  body { position: relative; font-family: "Montserrat", sans-serif; }

  .label {
    position: absolute; left: 50px; top: 394px;
    width: 1114px; height: 411px; background: var(--paper);
  }
  .band {
    position: absolute; left: 0; width: 100%;
    background: linear-gradient(90deg, var(--deep) 0%, var(--navy) 12%, var(--violet) 38%, var(--purple) 55%, var(--violet) 75%, var(--navy) 100%);
  }
  .band--top { top: 0; height: 33px; }
  .band--bottom { bottom: 0; height: 56px; color: #fff; }

  .info { position: absolute; left: 39px; top: 73px; width: 205px; font-size: 8.4px; line-height: 1.28; color: var(--navy); font-weight: 300; }
  .info p { margin-bottom: 10px; }
  .info strong { font-weight: 600; }
  .info .caution { font-weight: 700; text-transform: uppercase; }
  .disclaimer { position: absolute; left: 40px; top: 313px; width: 210px; text-align: center; font-family: "Oswald", sans-serif; font-weight: 500; font-size: 7px; line-height: 1.35; color: var(--navy); letter-spacing: -0.1px; }

  .badges { position: absolute; left: 347px; top: 58px; display: flex; flex-direction: column; gap: 20px; }
  .badge { width: 56px; height: 56px; border-radius: 50%; }
  .badge--gold { background: radial-gradient(circle at 40% 35%, #f4d35e, var(--gold) 60%, #9b6b0c); }
  .badge--green { background: radial-gradient(circle at 40% 35%, #47a55c, var(--green) 65%, #0f4b22); }
  .badge--seal { background: radial-gradient(circle at 40% 35%, #f4d35e, var(--gold) 55%, var(--ribbon) 100%); }
  .badge--navy { background: radial-gradient(circle at 40% 35%, #2d3c8c, var(--navy) 65%, var(--ribbon) 100%); }

  .brand { position: absolute; left: 404px; top: 42px; width: 300px; text-align: center; }
  .brand__art {
    width: 160px; height: 160px; margin: 0 auto;
    background: linear-gradient(180deg, var(--tree-red) 0%, #b52a4c 45%, var(--tree-plum) 100%);
    border-radius: 50% 50% 12% 12% / 58% 58% 12% 12%;
  }
  .brand__name { margin-top: 8px; font-size: 28px; font-weight: 700; color: var(--violet); letter-spacing: -0.5px; line-height: 1.1; white-space: nowrap; }
  .product { position: absolute; left: 404px; top: 268px; width: 300px; text-align: center; }
  .product__title { font-size: 31px; font-weight: 800; color: var(--purple); line-height: 1; }
  .product__sub { margin-top: 5px; font-size: 15px; line-height: 18px; font-weight: 300; letter-spacing: 0.5px; color: var(--purple); }
  .product__count { margin-top: 10px; font-size: 14px; line-height: 16px; font-weight: 700; color: var(--purple); letter-spacing: 0.3px; }

  .band__lot { position: absolute; left: 46px; top: 22px; font-family: "Oswald", sans-serif; font-size: 8.5px; font-weight: 500; }
  .band__title { position: absolute; left: 404px; width: 300px; top: 10px; text-align: center; font-family: "Oswald", sans-serif; font-weight: 600; font-size: 24px; letter-spacing: 0.2px; }
  .band__dist { position: absolute; left: 784px; top: 25px; font-family: "Oswald", sans-serif; font-size: 8px; font-weight: 500; }
  .band__brand { position: absolute; left: 938px; top: 15px; font-family: "Oswald", sans-serif; font-weight: 600; font-size: 18px; }

  .facts { position: absolute; left: 784px; top: 57px; width: 282px; height: 287px; border: 2px solid var(--ink); padding: 6px 10px 0 18px; color: var(--ink); }
  .facts__head { display: flex; align-items: flex-start; gap: 8px; margin-bottom: 2px; }
  .facts__title { font-size: 14px; font-weight: 600; letter-spacing: 0.2px; line-height: 1.1; }
  .facts__serving { font-size: 6px; line-height: 1.3; margin-top: 2px; }
  .facts__serving b { font-weight: 700; }
  .facts table { border-collapse: collapse; font-size: 11.8px; font-weight: 300; }
  .facts td { padding: 0; height: 14px; line-height: 14px; white-space: nowrap; }
  .facts td:first-child { width: 137px; }
</style>
</head>
<body>
<main class="label">
  <div class="band band--top"></div>

  <section class="info">
    <p><strong>Directions:</strong> As a dietary supplement, take two (2) capsules in the morning with meal.<br>Warning: Consult with a physician prior to use if you have a medical contition.</p>
    <p><strong>Morvel &amp; Morvel Multi Vitamin</strong> provides the perfect amount of vitamins, minerals, antioxidants, and herbs. In today's fast-paced world, many people don't get the daily recommended allowance of vitamins, minerals and other nutrients. Morvel &amp; Morvel helps to bridge the nutrient gap in your diet. It offers immune support, increased energy, and mental alertness by providing your body with all it needs. Get exaclty what you need with a formula that is made specifically for you.*</p>
    <p class="caution">Keep out of reach of children. Do not use if safety seal is damaged or missing, store in a cool , dry place.</p>
  </section>
  <p class="disclaimer">*These statements have not been evaluated by the Food and Drug Administration. This product is not intended to diagnose, teat, cure or prevent any disease.</p>

  <div class="badges">
    <div class="badge badge--gold"></div>
    <div class="badge badge--green"></div>
    <div class="badge badge--seal"></div>
    <div class="badge badge--navy"></div>
  </div>

  <div class="brand">
    <div class="brand__art" role="img" aria-label="Tree illustration in red to purple gradient"></div>
    <div class="brand__name">Morvel &amp; Morvel</div>
  </div>

  <div class="product">
    <h1 class="product__title">Multi Vitamin</h1>
    <p class="product__sub">NATURAL HEALING</p>
    <p class="product__count">50 CAPSULES</p>
  </div>

  <section class="facts">
    <div class="facts__head">
      <h2 class="facts__title">SUPPLEMENT FACTS</h2>
      <div class="facts__serving"><b>Serving Size:</b> 2 Capsules<br><b>Servings Per Container:</b> 50</div>
    </div>
    <table>
      <tr><td>Liquid Magna-Min</td><td>(400 mg) 4 oz</td></tr>
      <tr><td>Liquid Ionic B12</td><td>(1,000 mcg) 2 oz</td></tr>
      <tr><td>Probiotic 55</td><td>Billion 30 CT</td></tr>
      <tr><td>Liquid Potassium</td><td>99mg</td></tr>
      <tr><td>Liquid Iodide</td><td>225mcg</td></tr>
      <tr><td>Liquid Strontium</td><td>100 mg</td></tr>
      <tr><td>Liquid Iron</td><td>22mg</td></tr>
      <tr><td>Liquid Ionic Zinc</td><td>(50 mg) 2 oz</td></tr>
      <tr><td>Liquid Ionic Selenium</td><td>(300 mcg) 2 oz</td></tr>
      <tr><td>Lonic Boron</td><td>6 mg</td></tr>
      <tr><td>Fulvic Acid</td><td>250 mg</td></tr>
      <tr><td>Chromium</td><td>550 mcg</td></tr>
      <tr><td>Ox Bile</td><td>500 mg</td></tr>
      <tr><td>Vitamin D3</td><td>D3 1000 IU</td></tr>
      <tr><td>Liver Support</td><td>1000 IU</td></tr>
      <tr><td>Tonify blood</td><td>1000 IU</td></tr>
      <tr><td>Adrenal Support</td><td>1000 IU</td></tr>
      <tr><td>Constipation</td><td>1000 IU</td></tr>
    </table>
  </section>

  <div class="band band--bottom">
    <span class="band__lot">Lot# and Expiration Date Printed on bottom of Bottle</span>
    <span class="band__title">DIETARY SUPPLEMENT</span>
    <span class="band__dist">Distributed by:</span>
    <span class="band__brand">Morvel &amp; Morvel</span>
  </div>
</main>
</body>
</html>
```